Mini Book (4.25 x 6) Cover Design for Christian authors

We need a book cover designed for a mini book (4.25 x 6). We will need a front, back and spine for the book.
The book is titled:
Harbor Lanterns
Subtitle:
Quiet Light Along Your Path
Authors:
Walter and Renata Oskarsby
We are wanting the colors Dark Blue and Grey with more blue than grey.
We do not want any stock images or photos, only original work.
The cover should convey sincerity, intuition and truth with prestige.
We want the back cover text to be included (top) and the bios to be on the back as well (bottom). *Those documents are included in the files.
Since it is a mini book, it is important for the design to be simple and not cluttered, but powerful!
This is the first book in a twelve book series, so we would like the same "look" to carry through all twelve books, eventually.
On the back of the book, at the bottom (left), we want the following contact information:
Bright Meadow Method Logo (in files below)
tallwillowstudio@mailfernly.com
303.512.4086
P.O.Box 718
Larkmoor, NM 80417

Please save room on the back (bottom-right) for the ISBN and price.
Updates

Thank you to the designers that have submitted feedback concerning our design brief. We have made some changes that will perhaps make it easier to submit a variety of designs.Thank you! Added Saturday, March 4, 2017

Target Market(s)

Christians - mainly women

Industry/Entity Type

Religious

Font styles to use
Serif
Sans Serif
Decorative
Script
Other font styles liked:
• Not any particular font, looking for one that goes well with the cover design.

Requirements
Must have
• Mini Book Size (4.25 x 6)-spine size 1/8" (0.125)
• Dark blue and grey colors
• Cover needs to be simple and not cluttered or busy.
• Intriguing
• A font that is attractive, but it is still easy to read.
• *File information below
Nice to have
• Designs that are different from the mainstream.
• Perhaps a design that would do something different with the title/font? Maybe a repeat of the words from smaller to larger? Not sure how it would look, but maybe?
Should not have
• Any other colors but dark blue and grey
• Cluttered Look

```html
<!DOCTYPE html>
<html lang="en">
<head>
<meta charset="utf-8">
<title>Harbor Lanterns – Book Cover</title>
<link href="https://fonts.googleapis.com/css2?family=Bebas+Neue&family=Yellowtail&family=Tinos:ital,wght@0,400;0,700;1,400;1,700&display=swap" rel="stylesheet">
<style>
  :root {
    --page: #ffffff;
    --navy-deep: #0f2547;
    --navy: #1b3d6b;
    --blue-mid: #2f5a8c;
    --blue-light: #4f7cab;
    --band-grey: #6a6b76;
    --ink-white: #ffffff;
    --ink-blue: #1b3d6b;
  }
  * { margin: 0; padding: 0; box-sizing: border-box; }
  html, body { width: 1200px; height: 841px; overflow: hidden; background: var(--page); }
  .canvas { position: relative; width: 1200px; height: 841px; }

  .cover {
    position: absolute; left: 25px; top: 25px; width: 1150px; height: 790px;
    background:
      radial-gradient(ellipse at 30% 20%, rgba(79,124,171,.55), transparent 60%),
      radial-gradient(ellipse at 80% 15%, rgba(79,124,171,.5), transparent 55%),
      radial-gradient(ellipse at 60% 80%, rgba(47,90,140,.5), transparent 60%),
      linear-gradient(180deg, var(--navy) 0%, var(--navy-deep) 100%);
    overflow: hidden;
  }
  .fold { position: absolute; top: 0; width: 1px; height: 100%; background: rgba(255,255,255,.15); }

  .band { position: absolute; background: var(--band-grey); }
  .band--back-mid { left: 0; top: 343px; width: 600px; height: 42px; }
  .band--front-mid { left: 600px; top: 343px; width: 550px; height: 82px;
    background: linear-gradient(180deg, var(--band-grey) 0%, var(--band-grey) 60%, rgba(106,107,118,0) 100%); }
  .band--back-foot { left: 0; top: 680px; width: 600px; height: 110px;
    background: linear-gradient(180deg, var(--band-grey) 0%, var(--band-grey) 40%, rgba(106,107,118,.15) 100%); }
  .band--front-foot { left: 600px; top: 718px; width: 550px; height: 50px;
    background: linear-gradient(180deg, var(--band-grey) 0%, var(--band-grey) 70%, rgba(106,107,118,0) 100%); }

  .front-art {
    position: absolute; left: 600px; top: 425px; width: 550px; height: 293px;
    background: radial-gradient(ellipse at 20% 20%, #6f8fb3 0%, #2c4f7c 40%, #112a4d 100%);
  }

  .back-blurb {
    position: absolute; left: 65px; top: 108px; width: 430px;
    font-family: "Bebas Neue", sans-serif; font-size: 18px; line-height: 26px;
    color: var(--ink-white); letter-spacing: .2px;
  }
  .back-blurb p { text-indent: 28px; }
  .back-blurb ul { list-style: none; padding-left: 38px; }

  .back-bio {
    position: absolute; left: 88px; top: 420px; width: 412px;
    font-family: "Tinos", serif; font-size: 16px; line-height: 20px; color: var(--ink-white);
  }
  .back-bio p { text-indent: 24px; }
  .back-bio blockquote { font-style: italic; padding-left: 24px; }

  .contact { position: absolute; left: 42px; top: 677px; display: flex; gap: 10px; }
  .contact-mark {
    width: 80px; height: 78px; background: var(--ink-white);
    display: flex; align-items: center; justify-content: center; text-align: center;
    font-family: "Tinos", serif; font-weight: 700; font-size: 12px; line-height: 14px;
    color: var(--ink-blue); padding: 6px;
  }
  .contact-lines {
    font-family: "Tinos", serif; font-weight: 700; font-size: 13px; line-height: 16px;
    color: var(--ink-white); padding-top: 14px; font-style: normal;
  }

  .spine-title {
    position: absolute; left: 583px; top: 112px;
    transform-origin: left top; transform: rotate(90deg);
    white-space: nowrap; color: var(--ink-white); line-height: 1;
  }
  .spine-title .sans { font-family: "Bebas Neue", sans-serif; font-size: 30px; letter-spacing: 1px; }
  .spine-title .script { font-family: "Yellowtail", cursive; font-size: 28px; margin-left: 8px; }
  .spine-mark { position: absolute; left: 558px; top: 702px; width: 28px; height: 28px;
    border-radius: 50%; background: var(--ink-white); }

  .front-title { position: absolute; left: 640px; top: 100px; width: 480px; text-align: center; color: var(--ink-white); font-weight: 400; }
  .front-title .sans {
    display: block; font-family: "Bebas Neue", sans-serif; font-size: 150px; line-height: 120px;
    letter-spacing: 2px; text-shadow: 0 4px 8px rgba(0,0,0,.45);
  }
  .front-title .script {
    display: block; font-family: "Yellowtail", cursive; font-size: 112px; line-height: 130px;
    margin-top: -4px; text-shadow: 0 4px 8px rgba(0,0,0,.45);
  }
  .subtitle {
    position: absolute; right: 90px; top: 344px;
    font-family: "Bebas Neue", sans-serif; font-size: 24px; letter-spacing: .5px; color: var(--ink-white);
  }
  .authors {
    position: absolute; right: 52px; top: 722px;
    font-family: "Bebas Neue", sans-serif; font-size: 24px; letter-spacing: .6px; color: var(--ink-white);
  }
</style>
</head>
<body>
<div class="canvas">
  <div class="cover">
    <div class="band band--back-mid"></div>
    <div class="band band--front-mid"></div>
    <div class="band band--back-foot"></div>
    <div class="band band--front-foot"></div>
    <div class="front-art" role="img" aria-label="Footprints in dark blue sand leading up toward a walking figure"></div>
    <div class="fold" style="left:535px"></div>
    <div class="fold" style="left:600px"></div>

    <section class="back-blurb">
      <p>Bright Meadow Method (BMM)® proceeds, prepares and propels us into our divine inheritance. God always has our best interest at heart. By understanding His power, we are able to significantly impact the lives of others, leaving our imprint upon their hearts.</p>
      <p>This book will:</p>
      <ul>
        <li>Uncover the secret that is God’s plan</li>
        <li>Unveil God’s six significant shields</li>
        <li>Unmask God’s positioning strategy (GPS)</li>
      </ul>
    </section>

    <section class="back-bio">
      <p><strong><em>International award winning authors,</em></strong> Renata and Walter Oskarsby inspire couples and individuals to connect to the heart of God through <strong>Bright Meadow Method</strong>®. For over twenty years, they have conducted workshops and seminars throughout the country and at their private retreat center located in the Tallrock mountains.</p>
      <blockquote>“Come, let us go up to the mountain of the LORD,<br>To the house (temple) of the God of Jacob;<br>That He may teach us His ways<br>And that we may walk in His paths.” ~ Isaiah 2:3</blockquote>
    </section>

    <div class="contact">
      <div class="contact-mark">Bright Meadow Method</div>
      <address class="contact-lines">
        tallwillowstudio@mailfernly.com<br>
        303.512.4086<br>
        P.O.Box 718<br>
        Larkmoor, NM 80417
      </address>
    </div>

    <div class="spine-title"><span class="sans">HARBOR</span><span class="script">Lanterns</span></div>
    <div class="spine-mark"></div>

    <h1 class="front-title"><span class="sans">HARBOR</span><span class="script">Lanterns</span></h1>
    <p class="subtitle">Quiet Light Along Your Path</p>
    <p class="authors">Walter and Renata Oskarsby</p>
  </div>
</div>
</body>
</html>
```